Income Tax and Accounting Brochure

I need a brochure using my new logo (file attached). I do tax work and accounting work. I am an EA (QDX Enrolled Agent - logo attached) and would like this incorporated into the brochure. I also have a MSA in Accounting. Please incorporate the text that I have provided in the brochure.

Target Market(s)

Tax Clients - both business and individuals

Industry/Entity Type

Accounting

Colors
0054AA
0677BA
7BADD7
CADEEF
E8F1F8

Requirements
Must have
• Use my logo and the QDX EA file in the brochure
Nice to have
• I would like to see a brochure that I can customize with my own text if possible.

```html
<!DOCTYPE html>
<html lang="en">
<head>
<meta charset="utf-8">
<title>Marlow Tax &amp; Accounting – Trifold Brochure</title>
<link href="https://fonts.googleapis.com/css2?family=Montserrat:wght@400;600;700;800&family=Open+Sans:wght@400;600&display=swap" rel="stylesheet">
<style>
  :root{
    --blue-deep:#0054AA;
    --blue-mid:#0677BA;
    --blue-soft:#7BADD7;
    --blue-pale:#CADEEF;
    --blue-mist:#E8F1F8;
    --navy:#0d2b5c;
    --red:#c8202f;
    --white:#ffffff;
    --stage:#e6e7e9;
    --ink:#33404f;
  }
  *{box-sizing:border-box;margin:0;padding:0}
  html,body{width:900px;height:1200px;overflow:hidden}
  body{background:var(--stage);font-family:"Open Sans",Arial,sans-serif;color:var(--ink)}
  .spread{position:absolute;left:0;top:220px;width:900px;height:760px;display:flex;box-shadow:0 8px 24px rgba(0,0,0,.18)}
  .panel{position:relative;width:300px;height:760px;overflow:hidden;background:var(--white)}
  .heading{font-family:"Montserrat",Arial,sans-serif;font-weight:800}
  .body-copy{font-size:11.5px;line-height:1.6}
  .photo{position:absolute}
  .curve{position:absolute;left:0;width:100%}

  /* About panel */
  .about .heading{position:absolute;left:26px;top:30px;width:250px;color:var(--blue-deep);font-size:19px;line-height:1.25}
  .about .intro{position:absolute;left:26px;top:100px;width:250px}
  .about .portrait{left:26px;top:300px;width:96px;height:118px;background:linear-gradient(160deg,var(--blue-pale),#8a99ad);border:3px solid var(--white);box-shadow:0 2px 6px rgba(0,0,0,.2)}
  .about .aside{position:absolute;left:134px;top:304px;width:142px;font-size:10.5px}
  .about .curve{top:440px;height:320px}
  .about .closing{position:absolute;left:26px;top:540px;width:250px;color:var(--white)}
  .about .web{position:absolute;left:0;bottom:22px;width:100%;text-align:center;color:var(--white);font-family:"Montserrat",Arial,sans-serif;font-weight:600;font-size:12px}

  /* Firm panel */
  .firm{background:var(--blue-deep);color:var(--white)}
  .firm .band{position:absolute;left:0;top:0;width:100%;height:72px;background:var(--navy);display:flex;align-items:center;justify-content:center}
  .firm .band .heading{font-size:20px;letter-spacing:.5px}
  .firm .intro{position:absolute;left:26px;top:96px;width:250px}
  .firm .services{position:absolute;left:26px;top:200px;width:250px;list-style:none;font-size:11.5px;line-height:1.9}
  .firm .services li::before{content:"";display:inline-block;width:7px;height:7px;background:var(--red);margin-right:9px;vertical-align:1px}
  .firm .card{position:absolute;left:0;top:390px;width:100%;height:370px;background:var(--white);color:var(--ink)}
  .firm .brand{position:absolute;left:26px;top:30px;display:flex;align-items:center;gap:10px}
  .brand-dot{width:30px;height:30px;border-radius:50%;background:var(--blue-deep)}
  .brand-name{font-family:"Montserrat",Arial,sans-serif;font-weight:700;color:var(--blue-deep);font-size:14px;line-height:1.2}
  .firm .contact{position:absolute;left:26px;top:110px;width:250px;font-size:12px;line-height:1.8}
  .firm .contact strong{font-family:"Montserrat",Arial,sans-serif;color:var(--navy)}
  .firm .contact svg{width:12px;height:12px;vertical-align:-1px;margin-right:6px;fill:var(--red)}
  .firm .badge{position:absolute;left:26px;bottom:36px;width:70px;height:70px;border-radius:50%;background:var(--blue-pale);border:3px solid var(--blue-mid)}

  /* Cover panel */
  .cover .brand{position:absolute;left:28px;top:32px;display:flex;align-items:center;gap:10px}
  .cover .hero{left:40px;top:130px;width:220px;height:220px;border-radius:50%;background:radial-gradient(circle at 45% 40%,#e8d9cc,#8f9fb6 70%,#6a7890);border:5px solid var(--white);box-shadow:0 3px 10px rgba(0,0,0,.2)}
  .cover .curve{top:90px;height:360px}
  .cover .tagline{position:absolute;left:0;top:500px;width:100%;text-align:center}
  .cover .firm-name{font-family:"Montserrat",Arial,sans-serif;font-weight:600;color:var(--navy);font-size:15px}
  .cover .slogan{color:var(--red);font-size:30px;margin-top:6px}
  .cover .web-bar{position:absolute;left:0;top:600px;width:100%;height:36px;background:var(--blue-deep);color:var(--white);display:flex;align-items:center;justify-content:center;font-family:"Montserrat",Arial,sans-serif;font-weight:600;font-size:13px}
  .cover .foot{position:absolute;left:0;bottom:0;width:100%;height:22px;background:var(--red)}
</style>
</head>
<body>
<main class="spread">

  <section class="panel about">
    <h2 class="heading">About Dana R. Ellery, MSA EA (Principal)</h2>
    <p class="body-copy intro">Dana R. Ellery is a licensed Enrolled Agent with the QDX, holding a Master of Science in Accounting. She brings over fifteen years of experience preparing returns and advising small businesses, families and individuals on every stage of their financial lives.</p>
    <div class="photo portrait" role="img" aria-label="Portrait photograph of the firm principal"></div>
    <p class="body-copy aside">Enrolled Agents are federally authorized to represent taxpayers before the QDX in audits, collections and appeals.</p>
    <svg class="curve" viewBox="0 0 300 320" preserveAspectRatio="none" aria-hidden="true">
      <path d="M0 40 Q150 -10 300 30 L300 320 L0 320 Z" fill="var(--red)"/>
      <path d="M0 62 Q150 14 300 52 L300 320 L0 320 Z" fill="var(--blue-deep)"/>
    </svg>
    <p class="body-copy closing">Whether you need year-round bookkeeping, payroll support or help with a notice, we answer your questions promptly and keep your records organized and secure.</p>
    <p class="web">www.marlowtax.example</p>
  </section>

  <section class="panel firm">
    <div class="band"><h2 class="heading">ASHGROVE, VA TAX FIRM</h2></div>
    <p class="body-copy intro">We are a full-service tax and accounting firm serving individuals and businesses across the region. Our services include:</p>
    <ul class="services">
      <li>Individual tax returns</li>
      <li>Business tax returns</li>
      <li>Bookkeeping &amp; payroll</li>
      <li>Tax planning</li>
      <li>QDX representation</li>
    </ul>
    <div class="card">
      <div class="brand">
        <span class="brand-dot"></span>
        <span class="brand-name">MARLOW TAX &amp;<br>ACCOUNTING, LLC</span>
      </div>
      <div class="contact">
        <p><svg viewBox="0 0 24 24"><path d="M12 2a7 7 0 0 0-7 7c0 5 7 13 7 13s7-8 7-13a7 7 0 0 0-7-7zm0 9.5A2.5 2.5 0 1 1 12 6a2.5 2.5 0 0 1 0 5.5z"/></svg>1420 Millbrook Rd<br><span style="padding-left:18px">Ashgrove, VA 20100</span></p>
        <p><svg viewBox="0 0 24 24"><path d="M6.6 10.8a15 15 0 0 0 6.6 6.6l2.2-2.2a1 1 0 0 1 1-.25 11.4 11.4 0 0 0 3.6.57 1 1 0 0 1 1 1V20a1 1 0 0 1-1 1A17 17 0 0 1 3 4a1 1 0 0 1 1-1h3.5a1 1 0 0 1 1 1c0 1.25.2 2.45.57 3.6a1 1 0 0 1-.25 1z"/></svg><strong>PHONE:</strong> (555) 010-4122</p>
        <p><svg viewBox="0 0 24 24"><path d="M6 3h12v5H6zM4 9h16a2 2 0 0 1 2 2v6h-4v4H6v-4H2v-6a2 2 0 0 1 2-2zm4 7v3h8v-3z"/></svg><strong>FAX:</strong> (555) 010-9660</p>
      </div>
      <div class="badge" aria-hidden="true"></div>
    </div>
  </section>

  <section class="panel cover">
    <div class="brand">
      <span class="brand-dot"></span>
      <span class="brand-name">MARLOW TAX &amp;<br>ACCOUNTING, LLC</span>
    </div>
    <svg class="curve" viewBox="0 0 300 360" preserveAspectRatio="none" aria-hidden="true">
      <path d="M0 250 Q120 330 300 230 L300 262 Q120 360 0 280 Z" fill="var(--red)"/>
      <path d="M0 278 Q120 360 300 262 L300 284 Q120 384 0 300 Z" fill="var(--blue-deep)"/>
    </svg>
    <div class="photo hero" role="img" aria-label="Photograph of two colleagues reviewing paperwork at a laptop"></div>
    <div class="tagline">
      <p class="firm-name">Marlow Tax &amp; Accounting, LLC</p>
      <h1 class="heading slogan">WE CAN HELP YOU</h1>
    </div>
    <div class="web-bar">www.marlowtax.example</div>
    <div class="foot"></div>
  </section>

</main>
</body>
</html>
```